Basic Letterhead Design

We need a Letterhead design. Our company is in the financial services industry. We are a small bank who lends money. I have uploaded an example our current letterhead design. We would like a new one.

```html
<!DOCTYPE html>
<html lang="en">
<head>
<meta charset="utf-8">
<title>Harlow Lending – Stationery</title>
<link href="https://fonts.googleapis.com/css2?family=Open+Sans:wght@400;600&display=swap" rel="stylesheet">
<style>
  :root {
    --bg: #e6e6e6;
    --paper: #f7f7f7;
    --brand: #325342;
    --ink: #5a5a5a;
    --ink-soft: #7a7a7a;
    --faint: #ececec;
  }
  * { box-sizing: border-box; margin: 0; padding: 0; }
  html, body { width: 1200px; height: 795px; overflow: hidden; }
  body {
    background: var(--bg);
    font-family: "Open Sans", sans-serif;
    position: relative;
  }
  .letterhead {
    position: absolute;
    left: 70px; top: 26px;
    width: 523px; height: 742px;
    background: var(--paper);
    box-shadow: 0 2px 10px rgba(0,0,0,.08);
    padding: 48px 54px 40px;
    overflow: hidden;
  }
  .letterhead > * { position: relative; z-index: 1; }
  .brand-mark {
    display: flex; align-items: center; justify-content: center; gap: 8px;
    margin-top: 6px;
  }
  .brand-mark .dot { width: 14px; height: 14px; border-radius: 50%; background: var(--brand); }
  .brand-name {
    color: var(--brand); font-weight: 600; font-size: 17px; letter-spacing: .06em;
  }
  .contact {
    list-style: none;
    margin: 26px 0 0 auto; width: 190px;
    font-size: 10px; line-height: 1.55; color: var(--ink-soft);
  }
  .contact li { display: flex; align-items: center; gap: 6px; }
  .contact svg { width: 9px; height: 9px; fill: var(--brand); flex: none; }
  .letter { margin-top: 20px; font-size: 9.6px; line-height: 1.55; color: var(--ink); }
  .salutation { margin-bottom: 8px; color: var(--ink-soft); }
  .letter p.body { text-indent: 30px; margin-bottom: 8px; text-align: justify; }
  .closing { margin-top: 6px; color: var(--ink-soft); }
  .signature {
    width: 90px; height: 44px; margin: 12px 0 0 4px;
    background: linear-gradient(90deg, #dcdcdc, #eeeeee);
    border-radius: 4px;
  }
  .sender { margin-top: 30px; font-size: 10.5px; line-height: 1.5; color: var(--ink-soft); }
  .sender .company { color: var(--brand); font-weight: 600; }
  .letterhead > .faint-circle {
    position: absolute; z-index: 0;
    right: 70px; bottom: -40px;
    width: 130px; height: 130px; border-radius: 50%; background: var(--faint);
  }
  .envelope {
    position: absolute;
    left: 640px; top: 250px;
    width: 500px; height: 270px;
    background: var(--paper);
    box-shadow: 0 2px 10px rgba(0,0,0,.08);
  }
  .envelope-flap {
    position: absolute; left: 0; right: 0; top: 0;
    height: 92px; background: var(--brand);
    border-radius: 0 0 18px 18px;
    display: flex; align-items: center; justify-content: center; gap: 8px;
  }
  .envelope-flap .dot { width: 12px; height: 12px; border-radius: 50%; background: var(--paper); }
  .envelope-flap .brand-name { color: var(--paper); font-size: 16px; }
</style>
</head>
<body>
  <section class="letterhead">
    <div class="faint-circle"></div>

    <header class="brand-mark">
      <span class="dot"></span>
      <span class="brand-name">HARLOW LENDING</span>
    </header>

    <ul class="contact">
      <li>ACN: 512 090 386</li>
      <li><svg viewBox="0 0 10 10"><path d="M2 1l2 2-1 1.2c.6 1.2 1.6 2.2 2.8 2.8L7 6l2 2-1.3 1.3C4.5 9 1 5.5.7 2.3z"/></svg>(555) 014-2276</li>
      <li><svg viewBox="0 0 10 10"><path d="M0 2h10v6H0zM.5 2.5 5 6l4.5-3.5"/></svg>hello@harlowlending.com</li>
      <li><svg viewBox="0 0 10 10"><circle cx="5" cy="5" r="5"/></svg>www.harlowlending.com</li>
    </ul>

    <article class="letter">
      <p class="salutation">Dear customer,</p>
      <p class="body">Lorem ipsum dolor sit amet, consectetur adipisicing elit, sed do eiusmod tempor incididunt ut labore et dolore magna aliqua. Ut enim ad minim veniam, quis nostrud exercitation ullamco laboris nisi ut aliquip ex ea commodo consequat. Duis aute irure dolor in reprehenderit in voluptate velit esse cillum dolore eu fugiat nulla pariatur. Excepteur sint occaecat cupidatat non proident, sunt in culpa qui officia deserunt mollit anim id est laborum.</p>
      <p class="body">Lorem ipsum dolor sit amet, consectetur adipisicing elit, sed do eiusmod tempor incididunt ut labore et dolore magna aliqua. Ut enim ad minim veniam, quis nostrud exercitation ullamco laboris nisi ut aliquip ex ea commodo consequat. Duis aute irure dolor in reprehenderit in voluptate velit esse cillum dolore eu fugiat nulla pariatur. Excepteur sint occaecat cupidatat non proident, sunt in culpa qui officia deserunt mollit anim id est laborum.</p>
      <p class="body">Lorem ipsum dolor sit amet, consectetur adipisicing elit, sed do eiusmod tempor incididunt ut labore et dolore magna aliqua. Ut enim ad minim veniam, quis nostrud exercitation ullamco laboris nisi ut aliquip ex ea commodo consequat. Duis aute irure dolor in reprehenderit in voluptate velit esse cillum dolore eu fugiat nulla pariatur. Excepteur sint occaecat cupidatat non proident, sunt in culpa qui officia deserunt mollit anim id est laborum.</p>
      <p class="body">Lorem ipsum dolor sit amet, consectetur adipisicing elit, sed do eiusmod tempor incididunt ut labore et dolore magna aliqua. Ut enim ad minim veniam, quis nostrud exercitation ullamco laboris nisi ut aliquip ex ea commodo consequat. Duis aute irure dolor.</p>
      <p class="closing">Yours Sincerely,</p>
      <div class="signature" role="img" aria-label="Handwritten signature of the sender"></div>
    </article>

    <footer class="sender">
      <p class="company">Harlow Lending Pty Ltd</p>
      <p>14 Fernvale Road,</p>
      <p>Oakridge, ON K2P 4T7</p>
    </footer>
  </section>

  <section class="envelope">
    <div class="envelope-flap">
      <span class="dot"></span>
      <span class="brand-name">HARLOW LENDING</span>
    </div>
  </section>
</body>
</html>
```